Harbor Business Cards

I need a business card designed with the following information.

Company Name: Harbor Wealth Management
Name: BriAnne Dockery
Title: Executive Assistant
Cell: (281) 555-0173
Direct Line: (832) 555-0148
Email: brianne@harborwmx.com
Address: 20537 W. Marlowe PKWY Ste. B
Tomball, TX 77390

I have attached the logo.
I would like it in navy blue and silver.
Thanks.

```html
<!DOCTYPE html>
<html lang="en">
<head>
<meta charset="utf-8">
<title>Harbor Wealth Management — Business Card</title>
<link href="https://fonts.googleapis.com/css2?family=Roboto:wght@400;700&display=swap" rel="stylesheet">
<style>
  :root {
    --navy: #0f1f3f;
    --navy-deep: #0a1428;
    --silver: #d4d6da;
    --ink: #3a3d44;
    --grey: #7b7e84;
    --paper: #ffffff;
    --backdrop: #e6e6e6;
  }
  * { margin: 0; padding: 0; box-sizing: border-box; }
  html, body {
    width: 1125px; height: 1200px; overflow: hidden;
    background: var(--backdrop);
    font-family: "Roboto", Arial, sans-serif;
  }
  .card {
    position: absolute; left: 150px; width: 826px; height: 471px; overflow: hidden;
  }
  .card--front { top: 98px; background: var(--paper); }
  .card--back { top: 631px; background: var(--navy); }

  .holder { position: absolute; left: 0; width: 440px; top: 120px; text-align: center; }
  .holder__name { font-size: 29px; font-weight: 700; color: var(--navy); letter-spacing: 0.5px; line-height: 1.1; }
  .holder__title { font-size: 20px; color: var(--grey); line-height: 1.2; }

  .feature {
    position: absolute; left: 0; top: 190px; width: 442px; height: 281px;
    background: linear-gradient(90deg, var(--navy) 60%, var(--navy-deep));
    display: flex; align-items: center; justify-content: center;
  }
  .feature__name {
    font-size: 46px; font-weight: 400; letter-spacing: 14px; text-transform: uppercase;
    color: var(--silver); padding-left: 14px;
  }

  .brand { position: absolute; text-align: center; font-weight: 400; text-transform: uppercase; }
  .brand__mark { display: block; margin: 0 auto; }
  .brand__name { display: block; }
  .brand__tag { display: block; }

  .brand--front { left: 450px; width: 376px; top: 55px; color: var(--navy); }
  .brand--front .brand__mark { width: 100px; height: 100px; background: var(--navy); }
  .brand--front .brand__name { margin-top: 32px; font-size: 30px; letter-spacing: 11px; padding-left: 11px; line-height: 34px; }
  .brand--front .brand__tag { margin-top: 4px; font-size: 12px; letter-spacing: 3.5px; padding-left: 3.5px; line-height: 16px; }

  .brand--back { left: 0; width: 826px; top: 140px; color: var(--silver); }
  .brand--back .brand__mark { width: 130px; height: 130px; background: var(--silver); }
  .brand--back .brand__name { margin-top: 26px; font-size: 36px; letter-spacing: 13px; padding-left: 13px; line-height: 42px; }
  .brand--back .brand__tag { margin-top: 6px; font-size: 14px; letter-spacing: 4px; padding-left: 4px; line-height: 18px; }

  .address {
    position: absolute; right: 54px; top: 266px; text-align: right; font-style: normal;
    font-size: 19px; color: var(--ink); line-height: 25px;
  }
  .contact { position: absolute; right: 52px; top: 331px; list-style: none; }
  .contact__item {
    display: flex; justify-content: flex-end; align-items: center; gap: 10px;
    font-size: 19px; color: var(--ink); height: 26.5px;
  }
  .contact__item--web { letter-spacing: 0.8px; }
  .contact__icon { width: 18px; height: 18px; fill: var(--navy); }
</style>
</head>
<body>
  <section class="card card--front">
    <div class="holder">
      <p class="holder__name">BRIANNE DOCKERY</p>
      <p class="holder__title">Executive Assistant</p>
    </div>
    <div class="feature" role="img" aria-label="Large navy brand feature for Harbor Wealth Management">
      <span class="feature__name">Harbor</span>
    </div>

    <div class="brand brand--front">
      <span class="brand__mark"></span>
      <span class="brand__name">Harbor</span>
      <span class="brand__tag">Wealth Management</span>
    </div>

    <address class="address">
      20537 W. Marlowe PKWY Ste. B<br>Tomball, TX 77390
    </address>

    <ul class="contact">
      <li class="contact__item">(832) 555-0148
        <svg class="contact__icon" viewBox="0 0 24 24"><path d="M6.6 10.8a15 15 0 0 0 6.6 6.6l2.2-2.2c.3-.3.7-.4 1-.2 1.1.4 2.3.6 3.6.6.6 0 1 .4 1 1V20c0 .6-.4 1-1 1A17 17 0 0 1 3 4c0-.6.4-1 1-1h3.5c.6 0 1 .4 1 1 0 1.3.2 2.5.6 3.6.1.3 0 .7-.2 1z"/></svg>
      </li>
      <li class="contact__item">(281) 555-0173
        <svg class="contact__icon" viewBox="0 0 24 24"><path d="M7 1h10a2 2 0 0 1 2 2v18a2 2 0 0 1-2 2H7a2 2 0 0 1-2-2V3a2 2 0 0 1 2-2zm0 3v14h10V4z"/></svg>
      </li>
      <li class="contact__item">brianne@harborwmx.com
        <svg class="contact__icon" viewBox="0 0 24 24"><path d="M2 5h20v14H2zm2 2v.5l8 5 8-5V7z"/></svg>
      </li>
      <li class="contact__item contact__item--web">www.harborwmx.com
        <svg class="contact__icon" viewBox="0 0 24 24"><circle cx="12" cy="12" r="10"/></svg>
      </li>
    </ul>
  </section>

  <section class="card card--back">
    <div class="brand brand--back">
      <span class="brand__mark"></span>
      <span class="brand__name">Harbor</span>
      <span class="brand__tag">Wealth Management</span>
    </div>
  </section>
</body>
</html>
```